Landing Page for z7 airport parking

The site will be called Q9 parking

We basically need a lead collector for airport parking. It should be a one page site with a form on it .

Info

Compare Cheap Airport Parking

Compare prices of car parking at all UK airports with our unbiased search engine and save money by booking in advance.

What we offer?

We are the cheapest that’s guaranteed! Q9 Parking compares cheap airport parking from almost all the car parks servicing UK airports plus…

Free comparison engine to find the best deal for you.
All types of car parking including Valet, Long Stay, Short Stay and Hotels with parking.
We guarantee you won’t find cheaper for the same product or service.
Your car parking space or hotel room is guaranteed.
Quick check out with prepaid vouchers.
Savings on published prices with easy and secure booking process.
What type of car parking?

There are four types of parking product we provide, On-Airport, Off-Airport, Valet Meet & Greet and Hotel parking.

On-Airport Parking

This is our most popular option. On-airport parking is the most convenient self park option. Its usually within a few minutes transfer time from the airport terminal and allows you to keep your car keys while abroad.

Off-Airport Parking

Similar to On-Airport parking but further away from the airport terminal making it less expensive. Also, the car park will keep your car keys so that they can block park your car in a secure compound. Transfer time to the airport is usually 10-15 minutes.

Meet & Greet Parking

This is the premium car parking service. You just drive up to the airport terminal to be met and greeted by a Valet Chauffeur who will park your car for you usually in one of the Off-Airport car parks. This is the most stress and hassle free option and great if you have lots of luggage or cumbersome items such as skis, snowboards, buggies etc.

Airport Hotel with Parking

If you’re worried about getting to the airport on time or have an early/late flight then booking into an airport hotel with parking the night before or after your flight is a very relaxing option. Especially if you have a long drive ahead of you, knowing that you can rest in a comfortable hotel before or after your flight is a most appealing option to some travellers. See it as an enjoyable extension to your holiday or business trip.

Target Market(s)

People travelling from a uk airport and will need parking

Industry/Entity Type

Airport

Font styles to use
Sans Serif

Requirements
Must have
• The form should ask.
• Flying From:
• Parking from:
• Returning to collect car
• Full Name:
• Address:
• Dob:
• Phone:
• And Search Button
Nice to have
• One Page Lading Page only No other pages everything should be on one page. Parallax is fine.

```html
<!DOCTYPE html>
<html lang="en">
<head>
<meta charset="utf-8">
<title>Q9 Parking – Compare Cheap Airport Parking</title>
<link href="https://fonts.googleapis.com/css2?family=PT+Sans+Narrow:wght@400;700&family=PT+Sans:ital,wght@1,400&display=swap" rel="stylesheet">
<style>
  :root{
    --blue:#0a8fc2;
    --blue-dark:#0577a6;
    --ink:#111;
    --muted:#666;
    --light:#ebebeb;
    --field:#fff;
  }
  *{box-sizing:border-box;margin:0;padding:0}
  html,body{width:941px;height:1200px;overflow:hidden;background:#fff}
  body{position:relative;font-family:"PT Sans Narrow","Arial Narrow",sans-serif;color:var(--ink)}
  .abs{position:absolute}

  /* header */
  .brand{left:139px;top:17px;display:flex;align-items:center;gap:8px;font-size:25px;color:var(--blue);font-weight:400}
  .brand-mark{width:29px;height:29px;background:var(--blue)}
  .nav{left:0;top:0}
  .nav-item{position:absolute;top:0;height:70px;display:flex;align-items:center;justify-content:center;font-size:13px;color:var(--ink)}
  .nav-item.tab{background:linear-gradient(110deg,#e4e4e4 0%,#f6f6f6 45%,#fff 100%)}
  .nav-item.active{color:var(--blue);font-weight:700}

  /* hero */
  .hero-title{left:138px;top:94px;font-size:55px;line-height:50px;font-weight:700;color:var(--blue);letter-spacing:-.5px}
  .hero-intro{left:147px;top:210px;width:300px;font-size:12.5px;line-height:14px}
  .benefits{left:155px;top:260px;width:320px;list-style:none;font-size:9.8px;letter-spacing:-.1px}
  .benefits li{height:18.6px;display:flex;align-items:center;gap:6px;white-space:nowrap}
  .benefits svg{width:8px;height:8px;flex:none}

  .offer-title{left:499px;top:102px;font-size:18px;font-weight:700;color:var(--blue)}
  .offer-text{left:499px;top:125px;width:310px;font-size:12.5px;line-height:17px}

  .search-form{left:485px;top:172px;width:326px;height:224px;background:linear-gradient(180deg,#f4f4f4,#e9e9e9);box-shadow:0 0 4px rgba(0,0,0,.12)}
  .field{position:absolute;left:0;width:326px;height:19px;display:flex;align-items:center}
  .field label{width:109px;text-align:right;font-size:12px;color:#555;padding-right:3px;white-space:nowrap}
  .field span{position:absolute;left:121px;width:186px;height:19px;background:var(--field);border:1px solid #e2e2e2;box-shadow:inset 0 1px 2px rgba(0,0,0,.05)}
  .search-btn{position:absolute;left:121px;top:185px;width:109px;height:26px;background:linear-gradient(180deg,#14a1d4,var(--blue-dark));color:#fff;font-weight:700;font-size:12.5px;display:flex;align-items:center;justify-content:center;gap:10px}

  /* types */
  .types-intro{left:150px;top:457px;font-size:12px;white-space:nowrap}
  .types-intro strong{color:var(--blue);font-size:15.5px;margin-right:4px}
  .product h2{font-size:20px;font-weight:700;line-height:24px}
  .product p{font-size:11.8px;line-height:14.6px;margin-top:5px}
  .book-btn{width:77px;height:18px;background:linear-gradient(180deg,#14a1d4,var(--blue-dark));color:#fff;font-size:9px;font-weight:700;display:flex;align-items:center;justify-content:center}

  /* footer band */
  .testimonial-band{left:0;top:958px;width:941px;height:218px;background:var(--light)}
  .band-shadow{left:180px;top:952px;width:380px;height:8px;background:radial-gradient(ellipse at center,rgba(0,0,0,.12),transparent 70%)}
  .quote-badge{left:333px;top:938px;width:30px;height:30px;border-radius:50%;background:#fff;box-shadow:0 0 4px rgba(0,0,0,.2);display:flex;align-items:center;justify-content:center;color:var(--blue);font-size:24px;font-weight:700;line-height:1;padding-top:8px}
  .avatar{left:149px;top:1004px;width:70px;height:74px;background:#fff;padding:3px;box-shadow:0 1px 4px rgba(0,0,0,.25)}
  .avatar div{width:100%;height:100%;background:linear-gradient(160deg,#c9d9e6,#8fb4cf)}
  .quote-text{left:251px;top:1011px;width:270px;font-family:"PT Sans",Arial,sans-serif;font-style:italic;font-size:9.6px;line-height:13px;color:#666}
  .author{left:150px;top:1100px;width:80px;text-align:center}
  .author-name{font-family:Georgia,serif;font-style:italic;font-size:13px;color:#444}
  .author-role{font-size:8px;color:var(--blue);font-weight:700}
  .dots{left:251px;top:1103px;display:flex;gap:3px}
  .dots i{width:8px;height:8px;border-radius:50%;background:#c9c9c9}
  .social{left:367px;top:1096px;display:flex;align-items:center;gap:3px;font-size:9px;color:#444}
  .social .label{margin-right:10px}
  .social i{width:18px;height:18px;border-radius:3px;background:var(--blue-dark)}
  .divider{left:556px;top:983px;height:163px;border-left:1px dotted #888}
  .newsletter{left:598px;top:991px;width:200px;text-align:center}
  .newsletter h3{font-size:13.5px;color:var(--blue);font-weight:700}
  .newsletter p{font-size:12px;color:#777}
  .news-input{left:606px;top:1041px;width:186px;height:25px;background:#fff;border:1px solid #ddd}
  .news-note{left:614px;top:1079px;width:180px;font-family:"PT Sans",Arial,sans-serif;font-style:italic;font-size:7.4px;line-height:9.5px;color:#888}
  .subscribe-btn{left:645px;top:1122px;width:110px;height:26px;background:linear-gradient(180deg,#14a1d4,var(--blue-dark));color:#fff;font-weight:700;font-size:12.5px;display:flex;align-items:center;justify-content:center}

  .site-footer{left:0;top:1176px;width:941px;height:24px;background:var(--blue);color:#fff;font-size:8px}
  .site-footer .legal{position:absolute;left:133px;top:7px}
  .site-footer .copy{position:absolute;right:127px;top:7px}
</style>
</head>
<body>

<header>
  <div class="brand abs"><span class="brand-mark"></span>Q9 Parking</div>
  <nav class="nav abs">
    <div class="nav-item active" style="left:350px;width:74px">Home</div>
    <div class="nav-item tab" style="left:427px;width:92px">On Airport</div>
    <div class="nav-item tab" style="left:519px;width:94px">Off Airport</div>
    <div class="nav-item tab" style="left:613px;width:106px">Meet &amp; Greet</div>
    <div class="nav-item tab" style="left:719px;width:109px">Airport Hotel</div>
  </nav>
</header>

<section class="hero">
  <h1 class="hero-title abs">Compare Cheap<br>Airport Parking</h1>
  <p class="hero-intro abs">Compare prices of car parking at all UK airports with our unbiased search engine and save money by booking in advance.</p>
  <ul class="benefits abs">
    <li><svg viewBox="0 0 8 8"><path d="M1 4.5 3 6.5 7 1.5" fill="none" stroke="#222" stroke-width="1.4"/></svg>Free comparison engine to find the best deal for you.</li>
    <li><svg viewBox="0 0 8 8"><path d="M1 4.5 3 6.5 7 1.5" fill="none" stroke="#222" stroke-width="1.4"/></svg>All types of car parking including Valet, Long Stay, Short Stay and Hotels with parking.</li>
    <li><svg viewBox="0 0 8 8"><path d="M1 4.5 3 6.5 7 1.5" fill="none" stroke="#222" stroke-width="1.4"/></svg>We guarantee you won’t find cheaper for the same product or service.</li>
    <li><svg viewBox="0 0 8 8"><path d="M1 4.5 3 6.5 7 1.5" fill="none" stroke="#222" stroke-width="1.4"/></svg>Your car parking space or hotel room is guaranteed.</li>
    <li><svg viewBox="0 0 8 8"><path d="M1 4.5 3 6.5 7 1.5" fill="none" stroke="#222" stroke-width="1.4"/></svg>Quick check out with prepaid vouchers.</li>
    <li><svg viewBox="0 0 8 8"><path d="M1 4.5 3 6.5 7 1.5" fill="none" stroke="#222" stroke-width="1.4"/></svg>Savings on published prices with easy and secure booking process.</li>
  </ul>

  <h2 class="offer-title abs">What we offer?</h2>
  <p class="offer-text abs"><strong>We are the cheapest that’s guaranteed!</strong> Q9 Parking compares cheap airport parking from almost all the car parks servicing UK airports.</p>

  <form class="search-form abs">
    <div class="field" style="top:17px"><label>Flying From</label><span></span></div>
    <div class="field" style="top:40.5px"><label>Parking from</label><span></span></div>
    <div class="field" style="top:64px"><label>Returning to collect car</label><span></span></div>
    <div class="field" style="top:87.5px"><label>Full Name</label><span></span></div>
    <div class="field" style="top:111px"><label>Address</label><span></span></div>
    <div class="field" style="top:134.5px"><label>Dob</label><span></span></div>
    <div class="field" style="top:158px"><label>Phone</label><span></span></div>
    <div class="search-btn">
      <svg width="11" height="11" viewBox="0 0 11 11"><circle cx="4" cy="4" r="3" fill="none" stroke="#fff" stroke-width="1.6"/><path d="M6.2 6.2 10 10" stroke="#fff" stroke-width="2"/></svg>
      SEARCH NOW
    </div>
  </form>
</section>

<section class="types">
  <p class="types-intro abs"><strong>What type of car parking?</strong> There are four types of parking product we provide, On-Airport, Off-Airport, Valet Meet &amp; Greet and Hotel parking.</p>

  <article class="product abs" style="left:152px;top:527px;width:285px">
    <h2>On-Airport Parking</h2>
    <p>This is our most popular option. On-airport parking is the most convenient self park option. Its usually within a few minutes transfer time from the airport terminal and allows you to keep your car keys while abroad.</p>
    <div class="book-btn" style="margin-top:17px">BOOK NOW</div>
  </article>

  <article class="product abs" style="left:508px;top:527px;width:300px">
    <h2>Off-Airport Parking</h2>
    <p>Similar to On-Airport parking but further away from the airport terminal making it less expensive. Also, the car park will keep your car keys so that they can block park your car in a secure compound. Transfer time to the airport is usually 10-15 minutes.</p>
    <div class="book-btn" style="margin-top:17px">BOOK NOW</div>
  </article>

  <article class="product abs" style="left:152px;top:709px;width:295px">
    <h2>Meet &amp; Greet Parking</h2>
    <p style="margin-top:18px">This is the premium car parking service. You just drive up to the airport terminal to be met and greeted by a Valet Chauffeur who will park your car for you usually in one of the Off-Airport car parks. This is the most stress and hassle free option and great if you have lots of luggage or cumbersome items such as skis, snowboards, buggies etc.</p>
    <div class="book-btn" style="margin-top:14px">BOOK NOW</div>
  </article>

  <article class="product abs" style="left:508px;top:709px;width:275px">
    <h2>Airport Hotel with Parking</h2>
    <p style="margin-top:18px">If you’re worried about getting to the airport on time or have an early/late flight then booking into an airport hotel with parking the night before or after your flight is a very relaxing option. Especially if you have a long drive ahead of you, knowing that you can rest in a comfortable hotel before or after your flight is a most appealing option to some travellers. See it as an enjoyable extension to your holiday or business trip.</p>
    <div class="book-btn" style="margin-top:12px">BOOK NOW</div>
  </article>
</section>

<section class="testimonial-band abs"></section>
<div class="band-shadow abs"></div>
<div class="quote-badge abs">“</div>

<div class="avatar abs"><div role="img" aria-label="Portrait photo of a smiling customer"></div></div>
<p class="quote-text abs">Sed ut perspiciatis unde omnis iste natus sit voluptatem accusantium doloremque laudantium, totam rem aperiam, eaque ipsa quae ab illo inventore veritatis et quasi . Sed ut perspiciatis unde omnis iste natus sit voluptatem accusantium.</p>
<div class="author abs"><div class="author-name">- Sam Rowe</div><div class="author-role">Lorem Ipsum Elit</div></div>
<div class="dots abs"><i></i><i></i><i></i></div>
<div class="social abs"><span class="label">Get Social</span><i></i><i></i><i></i><i></i><i></i></div>
<div class="divider abs"></div>

<div class="newsletter abs">
  <h3>SUBSCRIBE TO OUR NEWSLETTER</h3>
  <p>Lorem Ipsum Consectetur Adipiscing Elit</p>
</div>
<div class="news-input abs"></div>
<p class="news-note abs">Sed ut perspiciatis unde omnis iste natus sit voluptatem accusantium. Sed ut perspiciatis unde omnis.</p>
<div class="subscribe-btn abs">SUBSCRIBE</div>

<footer class="site-footer abs">
  <span class="legal">Terms of Use | Privacy Policy</span>
  <span class="copy">Copyright © Q9 Parking 2014. All Rights Reserved.</span>
</footer>

</body>
</html>
```